AMAZING WEBSITE DESIGN NEEDED FOR MAID / CLEANING SERVICE

NOTE: This is Website Design Only - No coding required

Please submit your designs ASAP as we want to pick a winner and get started!

Hey,

We are looking for a new amazing website design for a maid or cleaning service.

They have a horrible website that we want turned into a masterpiece.

As you will see on their current site:

http://tidyhavenco.examplehost.net/

They have a lot of stuff, very disorganized, and need help.

Here is what we need:

Colors: Same as current site, Orange, Gray, Black

Menu: Horizontal with same Menu items

Need a spot for a video on the homepage

Want content to be structured in a great format that is easy to read.

Want to highlight commercial and residential on the website homepage.

Also want a spot for customer testimonials

We want the site clean, professional, fresh and modern.

Please help by matching the logo design.

I look forward to your designs!
Updates

Hi All! Really appreciate your efforts and designs. I will be meeting with our client on Monday and will then be able to provide feedback after our meeting. If you have other ideas, please submit them. The more I can show him the better! Thanks!

Target Market(s)

The target market is residential home owners as well as commercial businesses who need cleaning on a regular basis.

This company cleans homes and offices for individuals.

Industry/Entity Type

Residential

Font styles to use
Sans Serif

Requirements
Must have
• Must match logo colors
Must have spot for video
Must have a clean look
Must have a bold look
Nice to have
• Highly visual
Should not have
• clutter
messy design
hard to read

```html
<!DOCTYPE html>
<html lang="en">
<head>
<meta charset="utf-8">
<title>Tidy Haven – Home</title>
<link rel="stylesheet" href="https://fonts.googleapis.com/css2?family=Open+Sans:wght@300;400;600;700&display=swap">
<style>
:root{
  --orange:#f39129;
  --orange-dark:#e07a12;
  --ink:#222;
  --text:#3a3a3a;
  --muted:#6a6a6a;
  --rule:#e2e2e2;
  --footer:#505050;
  --footer-dark:#3e3e3e;
  --footer-text:#e8e8e8;
}
*{box-sizing:border-box;margin:0;padding:0}
html,body{width:733px;height:1200px;overflow:hidden;background:#fff}
body{position:relative;font-family:"Open Sans",sans-serif;color:var(--text)}
.abs{position:absolute}
a{color:inherit;text-decoration:none}

/* header */
.site-header{left:0;top:0;width:733px;height:72px;background:linear-gradient(#fff,#f4f4f4)}
.brand{left:24px;top:20px;display:flex;align-items:center;gap:7px}
.brand-mark{width:22px;height:22px;background:var(--orange)}
.brand-name{font-size:22px;font-weight:600;color:var(--orange);letter-spacing:-.3px;line-height:1}
.brand-tag{left:48px;top:47px;font-size:6.5px;color:var(--muted);font-weight:600}
.search{left:604px;top:14px;width:92px;height:12px;background:#e6e6e6;border-radius:2px;font-size:5.5px;color:#999;padding:2px 4px}
.search-icon{left:700px;top:15px}
.header-city{right:19px;top:32px;font-size:9.5px;color:var(--ink)}
.header-phone{right:19px;top:46px;font-size:16px;color:var(--orange);font-weight:400}

/* nav */
.main-nav{left:0;top:72px;width:733px;height:22px;background:linear-gradient(var(--orange),var(--orange-dark));display:flex;padding-left:25px}
.main-nav a{font-size:8px;color:#fff;line-height:22px;padding:0 4.6px}
.main-nav a.current{background:#f9a24a}

/* hero */
.hero{left:0;top:94px;width:733px;height:290px;
  background:
    radial-gradient(ellipse 30% 28% at 52% 38%, rgba(255,240,215,.7), transparent 70%),
    radial-gradient(ellipse 18% 30% at 88% 30%, rgba(255,225,180,.55), transparent 70%),
    radial-gradient(ellipse 22% 14% at 48% 74%, rgba(245,235,220,.65), transparent 75%),
    linear-gradient(90deg, rgba(70,40,20,.35) 0%, transparent 18%, transparent 82%, rgba(90,30,20,.3) 100%),
    linear-gradient(180deg,#dcc3a3 0%,#e8d5bb 18%,#c69d74 40%,#8d5f3d 58%,#b98a5c 70%,#a0714a 85%,#7a4e30 100%)}
.hero-band{left:0;top:355px;width:733px;height:29px;background:rgba(40,34,30,.88);display:flex;justify-content:space-between;align-items:center;padding:0 20px 0 26px;color:#fff;font-size:15px;font-weight:400}
.hero-band span{color:var(--orange)}

/* feature blocks */
.feature-photo{left:24px;width:201px;height:136px}
.photo-office{top:404px;background:radial-gradient(ellipse 50% 40% at 70% 30%,rgba(255,245,230,.8),transparent),linear-gradient(160deg,#f6ead9,#e3c9a6 45%,#a58b70 80%,#6f5c4a)}
.photo-home{top:562px;background:radial-gradient(ellipse 40% 45% at 75% 45%,rgba(230,240,220,.8),transparent),linear-gradient(160deg,#e5ddd2,#cbbba4 50%,#8f7c68 85%,#5f5246)}
.feature-label{right:0;bottom:0;background:rgba(20,20,20,.88);color:#fff;font-size:8.7px;padding:3px 5px}
.feature-label b{color:var(--orange);font-weight:400}
.block-title{font-size:15.5px;font-weight:400;color:var(--orange)}
.block-copy{font-size:7.3px;line-height:13px;color:var(--ink)}
.welcome{left:247px;top:403px;width:468px}
.welcome .block-copy{margin-top:3px}
.welcome .block-copy+.block-copy{margin-top:4px}
.divider-short{left:24px;top:550px;width:201px;height:1px;background:var(--rule)}
.local{left:247px;top:557px;width:216px}
.local h3{font-size:9.2px;font-weight:400;color:var(--ink);line-height:12px;margin-top:2px}
.local .block-copy{margin-top:3px}

/* video */
.video{left:487px;top:557px;width:227px;height:142px;background:#111;padding:2px}
.video-screen{width:223px;height:125px;background:radial-gradient(circle at 50% 50%,#b7d9ea,#86b8d3)}
.video-bar{left:2px;top:127px;width:223px;height:13px;background:#0c0c0c}

.divider-wide{left:24px;top:714px;width:690px;height:1px;background:var(--rule)}

/* testimonials */
.testimonials{left:24px;top:726px;width:199px}
.col-title{font-size:13px;font-weight:400;color:var(--ink)}
.t-date{font-size:9.5px;color:var(--orange);margin-top:4px}
.t-quote{font-size:7.3px;line-height:10.5px;color:var(--muted)}
.t-name{font-size:7.6px;color:var(--muted);margin-top:4px;text-transform:uppercase}
.t-rule{height:1px;background:var(--rule);margin:8px 0 5px}
.more{font-size:7.2px;color:var(--ink);margin-top:8px}

/* highlights */
.highlights{left:246px;top:728px;width:230px}
.hl-item{display:flex;align-items:center;gap:8px;height:52px;border-bottom:1px solid var(--rule)}
.hl-item:last-child{border-bottom:none}
.hl-icon{width:55px;height:44px;flex:none}
.hl-text{font-size:7.7px;line-height:10.3px;color:var(--ink)}
.hl-text b{display:block;color:var(--orange);font-weight:400;font-size:9.2px;line-height:11px}
.col-sep{left:488px;top:728px;width:1px;height:196px;background:var(--rule)}

/* ceo */
.ceo{left:505px;top:726px;width:210px}
.ceo .col-title{text-align:center}
.ceo-photo{width:64px;height:64px;border-radius:50%;margin:5px auto 0;background:radial-gradient(circle,#d9a889,#8e6a52);border:2px solid #cfcfcf}
.ceo-name{text-align:center;color:var(--orange);font-size:9px;margin-top:3px}
.ceo .t-quote{margin-top:2px}

/* photo strip */
.photo-strip{left:0;top:944px;width:733px;height:82px;display:flex;gap:1px;background:#fff}
.photo-strip div{flex:1}

/* footer */
.site-footer{left:0;top:1026px;width:733px;height:156px;background:var(--footer);color:var(--footer-text)}
.f-col{top:24px}
.f-col h4{font-size:9px;font-weight:400;color:#fff;margin-bottom:3px}
.f-col li{list-style:none;font-size:6.8px;line-height:13px}
.f-what{left:26px}
.f-contact{left:200px}
.social{display:flex;gap:4px;margin-top:8px}
.social span{width:15px;height:15px;background:var(--orange);border-radius:2px}
.f-news{left:392px}
.f-news h4{line-height:12px}
.news-input{left:393px;top:53px;width:209px;height:25px;background:#ddd;color:#777;font-size:8.6px;padding:6px 7px}
.news-submit{left:608px;top:53px;width:90px;height:25px;background:var(--orange);color:#fff;font-size:9.5px;font-weight:700;text-align:center;line-height:25px}
.bottom-bar{left:0;top:1182px;width:733px;height:18px;background:var(--footer-dark);color:#fff;font-size:6.8px;display:flex;justify-content:space-between;align-items:center;padding:0 19px 0 25px}
</style>
</head>
<body>

<header class="site-header abs">
  <div class="brand abs"><span class="brand-mark"></span><span class="brand-name">Tidy Haven</span></div>
  <div class="brand-tag abs">Quality Commercial &amp; Residential Cleaning</div>
  <div class="search abs">Search Site</div>
  <svg class="search-icon abs" width="9" height="9" viewBox="0 0 9 9"><circle cx="3.5" cy="3.5" r="2.5" fill="none" stroke="#f39129" stroke-width="1.3"/><line x1="5.4" y1="5.4" x2="8.3" y2="8.3" stroke="#f39129" stroke-width="1.6"/></svg>
  <div class="header-city abs">Albuquerque, New Mexico</div>
  <div class="header-phone abs">(505) 555-0182</div>
</header>

<nav class="main-nav abs">
  <a class="current">Home</a><a>Our Services</a><a>Our Employees</a><a>Why Choose Us?</a><a>What Our Customers are saying</a><a>Special Offers</a><a>About Us</a><a>Contact Us</a><a>Request a Bid</a><a>Meet the President &amp; CEO</a>
</nav>

<section class="hero abs" role="img" aria-label="Bright modern living room with city views, a fireplace and a wood floor"></section>
<div class="hero-band abs"><p>Wouldn’t it be nice, To come home to a perfectly clean house?</p><p>Call Now: <span>(505) 555-0182</span></p></div>

<div class="feature-photo photo-office abs" role="img" aria-label="Clean, sunlit commercial office">
  <div class="feature-label abs">Tidy Haven for <b>Commercial Offices</b></div>
</div>
<div class="divider-short abs"></div>
<div class="feature-photo photo-home abs" role="img" aria-label="Tidy residential living room">
  <div class="feature-label abs">Tidy Haven for <b>Residential Homes</b></div>
</div>

<section class="welcome abs">
  <h2 class="block-title">Welcome to Our Website</h2>
  <p class="block-copy">Thank you for visiting us! You are one step closer to experiencing first class maid service! Our company specializes in detailed housekeeping, janitorial, and commerical cleaning services making your environment shine and sparkle like it never has before! Our maids are fully trained professionals who we recruit from high end luxury hotels we know, like the Grand Crest and Bellmont! We pride ourselves in delivering exceptional service to our valued customers by fully understanding what your expectations &amp; needs are! We will strive for perfection and we will provide an uncompromising commitment to excellence!</p>
  <p class="block-copy">Our "haven" name gives us an edge over our competition by giving you access to more home and office cleaning services for absolutely no extra costs! Why pay more for less?? NEVER have any hidden charges, overages, or sneaky fees! With Tidy Haven start getting more for your dollar! Your wish is our command and that is the true "Haven" way! Call us today!</p>
</section>

<section class="local abs">
  <h2 class="block-title">Locally Owned &amp; Operated</h2>
  <h3>Never deal with an unresponsive franchise<br>Deal with the owner!</h3>
  <p class="block-copy">This is a company designed around the customer! We will make sure that you are accomodated in every way possible. It is our commitment to ensure that you have a clean, calm, and comfortable environment so you can relax, live, and work with a piece of mind. We will work very hard to make sure you experience the 'wow' factor when working with us! We truly are the new meaning of cleaning!</p>
</section>

<div class="video abs">
  <div class="video-screen" role="img" aria-label="Company introduction video"></div>
  <svg class="abs" style="left:95px;top:41px" width="40" height="40" viewBox="0 0 40 40"><circle cx="20" cy="20" r="19" fill="#111"/><path d="M15 11 L29 20 L15 29Z" fill="#fff"/></svg>
  <svg class="video-bar abs" viewBox="0 0 223 13"><rect x="2" y="3" width="7" height="7" fill="#eee"/><rect x="11" y="3" width="7" height="7" fill="#eee"/><rect x="20" y="3" width="7" height="7" fill="#eee"/><rect x="33" y="6" width="120" height="1.5" fill="#777"/><rect x="33" y="6" width="45" height="1.5" fill="#3a8fd0"/><rect x="160" y="4" width="22" height="4" fill="#555"/><rect x="186" y="3" width="9" height="7" fill="#e6c200"/><rect x="199" y="3" width="20" height="7" fill="#666"/></svg>
</div>

<div class="divider-wide abs"></div>

<section class="testimonials abs">
  <h2 class="col-title">What Our Customers are Saying</h2>
  <p class="t-date">January 2, 2014</p>
  <p class="t-quote">"I was very impressed with the amount they do for the price! Remarkable! Thank you Tidy Haven for taking this daily headache away from my fiance. She was so thrilled. See you guys again soon!</p>
  <p class="t-name">Calvin Reyes</p>
  <div class="t-rule"></div>
  <p class="t-date" style="margin-top:0">December 21, 2013</p>
  <p class="t-quote">"Thank you Tidy Haven for making my house so fresh and clean! How nice it was to have all of my laundry washed and folded and my dishes done and put away along with everything else! Paula was so pleasant to have in my home. I have requested that she return next week! Oustanding you guys, keep it up!</p>
  <p class="t-name">Loretta Banning</p>
  <p class="more">+ Read All</p>
</section>

<section class="highlights abs">
  <div class="hl-item"><div class="hl-icon" role="img" aria-label="Eco friendly green globe" style="background:radial-gradient(circle at 50% 55%,#7cc242 0 16px,transparent 17px)"></div><p class="hl-text">Tidy Haven is commited to using Eco Green chemicals to keep you and your family safe! No harsh chemicals here!</p></div>
  <div class="hl-item"><div class="hl-icon" role="img" aria-label="Happy local family" style="background:linear-gradient(90deg,#d6b398,#a97e60);height:24px"></div><p class="hl-text">Proudly serving our amazing customers in the Albuquerque Metro &amp; surrounding areas!</p></div>
  <div class="hl-item"><div class="hl-icon" role="img" aria-label="Pink awareness ribbon" style="background:radial-gradient(ellipse 8px 20px at 50% 50%,#f29bbf 90%,transparent 100%)"></div><p class="hl-text">Tidy Haven proudly donates 1% of its earnings to find a cure for breast cancer! Be part of a life changing cause!</p></div>
  <div class="hl-item"><div class="hl-icon" role="img" aria-label="Satisfaction guarantee seal" style="background:radial-gradient(circle,#c9a227 0 21px,transparent 22px)"></div><p class="hl-text"><b>Satisfaction Guaranteed!</b>We guarantee you will be 100% satisfied with our cleaning and our cleaning professionals!</p></div>
</section>
<div class="col-sep abs"></div>

<section class="ceo abs">
  <h2 class="col-title">Meet the President &amp; CEO</h2>
  <div class="ceo-photo" role="img" aria-label="Portrait of the company president"></div>
  <p class="ceo-name">Marcus D. Whitfield</p>
  <p class="t-quote">"I would like to personally thank you for considering Tidy Haven for your housekeeping and janitorial needs! It is my personal commitment that myself and my staff provide no less than our absolute best housekeeping and janotorial services that our industry has to offer. We will stop at nothing to make sure you are happy with our company, our staff, and our overall commitment to excellence....</p>
  <p class="more">+ Read Full Message</p>
</section>

<div class="photo-strip abs" role="img" aria-label="Gallery of cleaned homes and offices">
  <div style="background:radial-gradient(ellipse at 40% 30%,#f0dcc0,transparent 70%),linear-gradient(#c9a57d,#8e6a48)"></div>
  <div style="background:radial-gradient(ellipse at 60% 35%,#fbf1e4,transparent 70%),linear-gradient(#e4d0b6,#a88866)"></div>
  <div style="background:radial-gradient(ellipse at 50% 30%,#d8cbbb,transparent 70%),linear-gradient(#8f7c68,#4f433a)"></div>
  <div style="background:radial-gradient(ellipse at 60% 30%,#f4f2e6,transparent 70%),linear-gradient(#c9cdb6,#7f8466)"></div>
  <div style="background:radial-gradient(ellipse at 50% 25%,#eef2f6,transparent 70%),linear-gradient(#b7c2cd,#6f7c88)"></div>
  <div style="background:radial-gradient(ellipse at 50% 30%,#fafafa,transparent 70%),linear-gradient(#d4d6d6,#7e8488)"></div>
  <div style="background:radial-gradient(ellipse at 40% 30%,#f3f5f7,transparent 70%),linear-gradient(#c9ced3,#858d95)"></div>
  <div style="background:radial-gradient(ellipse at 50% 35%,#eadccb,transparent 70%),linear-gradient(#bba78f,#6f5d4a)"></div>
  <div style="background:radial-gradient(ellipse at 40% 30%,#dbe9a0,transparent 70%),linear-gradient(#a9c25a,#e08a30)"></div>
</div>

<footer class="site-footer abs">
  <div class="f-col f-what abs"><h4>What We Do</h4><ul><li>- Our Services</li><li>- Our Employees</li><li>- Why Choose Tidy Haven</li><li>- Special Offers</li><li>- About Us</li><li>- Request a Bid</li><li>- Meet the President &amp; CEO</li></ul></div>
  <div class="f-col f-contact abs"><h4>Contact Us</h4><ul><li>1420 Mesa Verde Road NE Suite 310</li><li>Albuquerque | New Mexico | 87100</li><li>(505) 555-0182 Office</li><li>(505) 555-0147 Fax</li><li>mwhitfield@tidyhaven.example</li></ul>
    <div class="social"><span></span><span></span><span></span><span></span><span></span></div></div>
  <div class="f-col f-news abs"><h4>Stay Up-to-date with our Newsletter<br>Sign Up Now</h4></div>
  <div class="news-input abs">Enter Email</div>
  <div class="news-submit abs">SUBMIT</div>
</footer>
<div class="bottom-bar abs"><p>Copyright © 2014 Tidy Haven | All Rights Reserved</p><p>Home | About Us | Contact Us</p></div>

</body>
</html>
```